Social-Business Application (iOS)

App is very simillar to "Murmel" from AppHarbor

Please see the wireframes!

We need a design for application according to attached wireframes.
Social-Business application is a mobile app, that let's user to login, using ProNexa and browse through other users content (meme's). There are 2 home pages and 4 categories (displayed in wireframes). They are pretty simillar to each other. First one is called "Say Something" and the other one called "Ask Something". On "Say Something" page user is able to browse through meme's with pictures. There are several options to each meme, as well as reply to meme with your own meme.
"Ask Something" has only 2 differences.
1. There are always "?" in the end of each meme.
2. Only plain background with different colors are acceptable.
User is also able to create meme's to each home page and category.

There is no First or Last name display! Only following info should be displayed:
Location, Industry, Number of ProNexa contacts.

There is also a simple chat function, that provides the ability to chat with author of the meme. On the chat preview we will show the meme preview Instead of profile picture.

Please, ask your questions.
Updates

Please, send your examples.

Please check out "Murmel" application for better understanding of the functionality and overall idea

https://apps.harborstore-example.com/store/apps/details?id=qz.murmel

I will report to our admin, to change Designer Payment to Commited if we will have at least one screen example from you, guys.

Target Market(s)

regular users, business users.
Adult Audience, Professional Audience.

Industry/Entity Type

Business

Font styles to use
Other font styles liked:
• Helvetica Neue

Requirements
Must have
• Design must have all screens and elements that are displayed in attached photos (wireframes).
Flat style is required.
Following the iOS guidelines is required.
Nice to have
• Design example could show different ui colors for each of home pages ("Ask Something" and "Say Something") to easily indicate on what home page user is.
Should not have
• The design should not be overloaded and should not use serif fonts like Times New Roman.

```html
<!DOCTYPE html>
<html lang="en">
<head>
<meta charset="utf-8">
<title>Social-Business App – Latest</title>
<link rel="stylesheet" href="https://fonts.googleapis.com/css2?family=Roboto:wght@400;500;700&family=Roboto+Condensed:wght@400&display=swap">
<style>
  :root{
    --brand:#29a9e1;
    --brand-deep:#1e6f9f;
    --canvas:#e6ebef;
    --card:#ffffff;
    --ink:#2b2b2b;
    --muted:#7b8790;
    --line:#d9dfe4;
    --white:#ffffff;
  }
  *{box-sizing:border-box;margin:0;padding:0}
  html,body{width:677px;height:1200px;overflow:hidden}
  body{position:relative;background:var(--canvas);font-family:"Roboto",Helvetica,Arial,sans-serif;color:var(--ink)}
  .status-bar{position:absolute;left:0;top:0;width:677px;height:45px;background:var(--brand);color:var(--white);font-size:24px;font-weight:500;display:flex;align-items:center;padding:0 12px}
  .status-bar .carrier{display:flex;align-items:center;gap:10px}
  .status-bar .time{position:absolute;left:0;right:0;text-align:center}
  .status-bar .right{margin-left:auto;display:flex;align-items:center;gap:10px}
  .nav-bar{position:absolute;left:0;top:45px;width:677px;height:95px;background:var(--brand);color:var(--white)}
  .nav-title{position:absolute;left:0;right:0;top:24px;text-align:center;font-size:36px;font-weight:700}
  .nav-menu{position:absolute;left:28px;top:24px}
  .nav-inbox{position:absolute;right:22px;top:26px}
  .badge{position:absolute;right:-8px;top:-10px;background:var(--white);color:var(--brand);font-size:16px;font-weight:700;border-radius:12px;padding:1px 6px}
  .pager{position:absolute;top:155px;left:0;right:0;display:flex;justify-content:center;gap:8px}
  .pager span{width:26px;height:26px;border-radius:50%;border:3px solid var(--brand);background:var(--white)}
  .pager span.active{background:var(--brand)}
  .card{position:absolute;width:320px;background:var(--card);overflow:hidden}
  .card-head{height:67px;padding:14px 14px 0;position:relative}
  .location{font-size:16px;font-weight:700}
  .industry{font-size:16px;font-weight:500;margin-top:8px}
  .contacts{position:absolute;right:14px;top:20px;display:flex;align-items:center;gap:8px;font-size:16px;font-weight:500}
  .meme{position:relative;display:flex;align-items:center;justify-content:center;padding:0 18px;text-align:center}
  .meme p{font-family:"Roboto Condensed","Arial Narrow",sans-serif;color:var(--white);font-size:32px;line-height:1.18;text-shadow:0 1px 3px rgba(0,0,0,.7)}
  .meme.tall{height:400px}
  .meme.short{height:220px}
  .stats{height:42px;display:flex;align-items:center;gap:16px;padding:0 12px;font-size:19px;color:var(--ink)}
  .stats .stat{display:flex;align-items:center;gap:6px}
  .drawer-tab{position:absolute;left:0;top:587px;width:22px;height:56px;background:var(--brand);border-radius:0 8px 8px 0;display:flex;align-items:center;justify-content:center}
  .ask-bar{position:absolute;left:11px;top:1106px;width:655px;height:56px;background:var(--brand-deep);color:var(--white);font-size:28px;font-weight:500;display:flex;align-items:center;padding-left:14px;border-radius:6px 6px 0 0}
</style>
</head>
<body>
  <div class="status-bar">
    <div class="carrier">
      <span>●●●●●</span><span>Carrier</span>
      <svg width="26" height="20" viewBox="0 0 26 20"><path d="M1 7a17 17 0 0 1 24 0M5 11a11 11 0 0 1 16 0M9 15a5 5 0 0 1 8 0" stroke="#fff" stroke-width="3" fill="none"/></svg>
    </div>
    <div class="time">12:34 AM</div>
    <div class="right">
      <svg width="18" height="20" viewBox="0 0 18 20"><path d="M1 9 17 1 11 19 9 11z" fill="#fff"/></svg>
      <svg width="14" height="22" viewBox="0 0 14 22"><path d="M2 6l10 10-5 5V1l5 5L2 16" stroke="#fff" stroke-width="2" fill="none"/></svg>
      <span>100%</span>
      <svg width="44" height="22" viewBox="0 0 44 22"><rect x="1" y="1" width="38" height="20" rx="4" fill="#fff"/><rect x="40" y="7" width="3" height="8" fill="#fff"/></svg>
    </div>
  </div>

  <header class="nav-bar">
    <svg class="nav-menu" width="44" height="44" viewBox="0 0 44 44"><g fill="none" stroke="#fff" stroke-width="3"><rect x="2" y="2" width="17" height="17"/><rect x="25" y="2" width="17" height="17"/><rect x="2" y="25" width="17" height="17"/><rect x="25" y="25" width="17" height="17"/></g></svg>
    <h1 class="nav-title">Latest</h1>
    <div class="nav-inbox">
      <svg width="44" height="34" viewBox="0 0 44 34"><rect x="2" y="2" width="40" height="30" fill="none" stroke="#fff" stroke-width="3"/><path d="M2 2l20 17L42 2" fill="none" stroke="#fff" stroke-width="3"/></svg>
      <span class="badge">10</span>
    </div>
  </header>

  <div class="pager"><span></span><span class="active"></span><span></span></div>

  <article class="card" style="left:11px;top:199px">
    <div class="card-head">
      <div class="location">Mumbai, IND</div>
      <div class="industry">Information Technology</div>
      <div class="contacts"><svg width="22" height="22" viewBox="0 0 22 22"><circle cx="11" cy="11" r="10" fill="none" stroke="#555" stroke-width="1.5"/><circle cx="11" cy="8" r="3" fill="#555"/><path d="M5 17c1-4 11-4 12 0" fill="#555"/></svg>300</div>
    </div>
    <div class="meme tall" role="img" aria-label="Background photo of a dim landscape at dusk" style="background:linear-gradient(160deg,#5d6468,#2e3438)">
      <p>I went to my friends' wedding the other day and the photographer caught me drinking out of my purse in the back of the church.</p>
    </div>
    <div class="stats">
      <span class="stat"><svg width="20" height="20" viewBox="0 0 20 20"><path d="M2 9h4v10H2zM7 9l4-8c2 0 2 2 2 3l-1 4h6c1 0 2 1 1 3l-2 7H7z" fill="none" stroke="#444" stroke-width="1.5"/></svg>324</span>
      <span class="stat"><svg width="20" height="20" viewBox="0 0 20 20"><path d="M2 3h16v11H8l-4 4v-4H2z" fill="none" stroke="#444" stroke-width="1.5"/></svg>226</span>
      <span class="stat"><svg width="20" height="20" viewBox="0 0 20 20"><circle cx="10" cy="10" r="8" fill="none" stroke="#444" stroke-width="1.5"/><path d="M10 5v5l3 3" fill="none" stroke="#444" stroke-width="1.5"/></svg>25.4.2014</span>
    </div>
  </article>

  <article class="card" style="left:339px;top:199px">
    <div class="card-head">
      <div class="location">Mumbai, IND</div>
      <div class="industry">Information Technology</div>
      <div class="contacts"><svg width="22" height="22" viewBox="0 0 22 22"><circle cx="11" cy="11" r="10" fill="none" stroke="#555" stroke-width="1.5"/><circle cx="11" cy="8" r="3" fill="#555"/><path d="M5 17c1-4 11-4 12 0" fill="#555"/></svg>300</div>
    </div>
    <div class="meme tall" role="img" aria-label="Background photo of a misty snowy field with bare trees" style="background:linear-gradient(180deg,#8f979b,#4d5357)">
      <p>I traveled 300 miles to be with my friends for my birthday and none of them showed up.</p>
    </div>
    <div class="stats">
      <span class="stat"><svg width="20" height="20" viewBox="0 0 20 20"><path d="M2 9h4v10H2zM7 9l4-8c2 0 2 2 2 3l-1 4h6c1 0 2 1 1 3l-2 7H7z" fill="none" stroke="#444" stroke-width="1.5"/></svg>324</span>
      <span class="stat"><svg width="20" height="20" viewBox="0 0 20 20"><path d="M2 3h16v11H8l-4 4v-4H2z" fill="none" stroke="#444" stroke-width="1.5"/></svg>226</span>
      <span class="stat"><svg width="20" height="20" viewBox="0 0 20 20"><circle cx="10" cy="10" r="8" fill="none" stroke="#444" stroke-width="1.5"/><path d="M10 5v5l3 3" fill="none" stroke="#444" stroke-width="1.5"/></svg>25.4.2014</span>
    </div>
  </article>

  <article class="card" style="left:11px;top:738px">
    <div class="card-head">
      <div class="location">Mumbai, IND</div>
      <div class="industry">Information Technology</div>
      <div class="contacts"><svg width="22" height="22" viewBox="0 0 22 22"><circle cx="11" cy="11" r="10" fill="none" stroke="#555" stroke-width="1.5"/><circle cx="11" cy="8" r="3" fill="#555"/><path d="M5 17c1-4 11-4 12 0" fill="#555"/></svg>300</div>
    </div>
    <div class="meme short" role="img" aria-label="Background photo of a person in warm indoor light" style="background:linear-gradient(160deg,#b88a6e,#6e4a3a)">
      <p>I throw away my worn out clothes because I don't want to see a poor person getting designer items for free.</p>
    </div>
    <div class="stats">
      <span class="stat"><svg width="20" height="20" viewBox="0 0 20 20"><path d="M2 9h4v10H2zM7 9l4-8c2 0 2 2 2 3l-1 4h6c1 0 2 1 1 3l-2 7H7z" fill="none" stroke="#444" stroke-width="1.5"/></svg>324</span>
      <span class="stat"><svg width="20" height="20" viewBox="0 0 20 20"><path d="M2 3h16v11H8l-4 4v-4H2z" fill="none" stroke="#444" stroke-width="1.5"/></svg>226</span>
      <span class="stat"><svg width="20" height="20" viewBox="0 0 20 20"><circle cx="10" cy="10" r="8" fill="none" stroke="#444" stroke-width="1.5"/><path d="M10 5v5l3 3" fill="none" stroke="#444" stroke-width="1.5"/></svg>25.4.2014</span>
    </div>
  </article>

  <article class="card" style="left:339px;top:738px">
    <div class="card-head">
      <div class="location">Mumbai, IND</div>
      <div class="industry">Information Technology</div>
      <div class="contacts"><svg width="22" height="22" viewBox="0 0 22 22"><circle cx="11" cy="11" r="10" fill="none" stroke="#555" stroke-width="1.5"/><circle cx="11" cy="8" r="3" fill="#555"/><path d="M5 17c1-4 11-4 12 0" fill="#555"/></svg>300</div>
    </div>
    <div class="meme short" role="img" aria-label="Background photo of a hotel window with silhouetted travellers" style="background:linear-gradient(180deg,#c9a46a,#5a4636)">
      <p>Whenever I stay at a high rise hotel I make sure to have sex against the open window.</p>
    </div>
    <div class="stats">
      <span class="stat"><svg width="20" height="20" viewBox="0 0 20 20"><path d="M2 9h4v10H2zM7 9l4-8c2 0 2 2 2 3l-1 4h6c1 0 2 1 1 3l-2 7H7z" fill="none" stroke="#444" stroke-width="1.5"/></svg>324</span>
      <span class="stat"><svg width="20" height="20" viewBox="0 0 20 20"><path d="M2 3h16v11H8l-4 4v-4H2z" fill="none" stroke="#444" stroke-width="1.5"/></svg>226</span>
      <span class="stat"><svg width="20" height="20" viewBox="0 0 20 20"><circle cx="10" cy="10" r="8" fill="none" stroke="#444" stroke-width="1.5"/><path d="M10 5v5l3 3" fill="none" stroke="#444" stroke-width="1.5"/></svg>25.4.2014</span>
    </div>
  </article>

  <article class="card" style="left:11px;top:1140px">
    <div class="card-head">
      <div class="location">Mumbai, IND</div>
      <div class="industry">Information Technology</div>
    </div>
  </article>
  <article class="card" style="left:339px;top:1140px">
    <div class="card-head">
      <div class="location">Mumbai, IND</div>
      <div class="industry">Information Technology</div>
    </div>
  </article>

  <div class="drawer-tab"><svg width="12" height="20" viewBox="0 0 12 20"><path d="M2 2l8 8-8 8" fill="none" stroke="#fff" stroke-width="3"/></svg></div>

  <div class="ask-bar">Ask something</div>
</body>
</html>
```